Harlow Solutions Website

My business has been word of mouth over the last 3 years and has grown. Now I need a website for additional marketing as we have new clients asking for a website.

You have already completed my Logo during an earlier project. I have attached the logo.

We do Staff Augmentation and Operation Support.

What is that?
Staff augmentation is an outsourcing strategy that allows companies to fill specific, temporary roles to achieve business objectives. This staffing method complements existing teams with specific talent, enhancing business capabilities or filling gaps left by members on extended leave.

We work alongside the internal recruiting team to assist clients to meet and exceed financial goals.

```html
<!DOCTYPE html>
<html lang="en">
<head>
<meta charset="utf-8">
<title>Harlow Solutions</title>
<link rel="stylesheet" href="https://fonts.googleapis.com/css2?family=Poppins:wght@400;500;600;700&display=swap">
<style>
:root{
  --navy:#0d3e6b;
  --navy-dark:#0a2f52;
  --ink:#1d1d1f;
  --text:#555b63;
  --heading:#111418;
  --light:#eef0f3;
  --white:#ffffff;
  --star:#e8a31c;
  --line:#e3e6ea;
  --placeholder:#d5d9de;
}
*{margin:0;padding:0;box-sizing:border-box}
html,body{width:1200px;height:3788px;overflow:hidden}
body{font-family:"Poppins",sans-serif;color:var(--text);background:var(--white);position:relative}
.abs{position:absolute}
a{color:inherit;text-decoration:none}

/* top bar */
.topbar{left:0;top:0;width:1200px;height:43px;background:var(--ink);color:#fff;font-size:11px;font-weight:500}
.topbar .info{left:110px;top:14px;display:flex;gap:14px;align-items:center}
.topbar .social{left:830px;top:13px;display:flex;gap:8px}
.dot-s{width:12px;height:12px;border-radius:50%;background:#fff}
.topbar .phone{left:915px;top:0;width:173px;height:43px;background:var(--navy);display:flex;align-items:center;justify-content:center;gap:8px}

/* header */
.header{left:0;top:43px;width:1200px;height:94px;background:#fff}
.brand{display:flex;align-items:center;gap:10px}
.brand .mark{width:46px;height:46px;border-radius:50%;background:var(--navy)}
.brand .name{font-weight:600;font-size:24px;color:var(--navy);line-height:1}
.header .brand{left:110px;top:24px}
.nav{right:112px;top:38px;display:flex;gap:36px;font-size:14px;font-weight:600;color:var(--heading)}
.nav .active{color:var(--navy);border-bottom:2px solid var(--navy);padding-bottom:6px}

/* hero */
.hero{left:0;top:137px;width:1200px;height:664px;overflow:hidden}
.hero .photo{left:0;top:0;width:1200px;height:664px;background:linear-gradient(100deg,#e9ece6 0%,#dfe3da 35%,#c9b9a6 55%,#8f8b86 75%,#6c6a67 100%)}
.hero h1{left:110px;top:190px;font-size:37px;font-weight:700;color:var(--heading);letter-spacing:-.3px}
.hero h1 span{color:var(--navy)}
.hero p{left:112px;top:245px;width:400px;font-size:16px;font-weight:600;line-height:27px;color:#2a2a2a}
.btn{display:inline-flex;align-items:center;justify-content:center;border-radius:26px;font-size:13px;font-weight:600;letter-spacing:.3px}
.btn-solid{background:var(--navy);color:#fff}
.btn-line{border:2px solid var(--ink);color:var(--navy);background:#fff}
.hero .btn{left:112px;top:322px;width:153px;height:48px}
.hero .wave{left:0;top:0}
.hero .dots{left:572px;top:575px;display:flex;gap:4px}
.ring{width:11px;height:11px;border-radius:50%;border:2px solid #fff}
.ring.on{background:#fff}

/* section titles */
.title{width:1200px;left:0;text-align:center;font-size:37px;font-weight:700;color:var(--heading)}
.title span{color:var(--navy)}

/* services */
.svc-lead{left:190px;top:940px;width:820px;text-align:center;font-size:14px;line-height:26px}
.svc-btns{left:382px;top:1022px;display:flex;gap:8px}
.svc-btns .btn{width:214px;height:50px}
.card{background:#fff;border:1px solid var(--line);box-shadow:0 2px 8px rgba(0,0,0,.12);border-radius:3px;text-align:center}
.svc{top:1119px;width:232px;height:318px}
.svc svg.ico{margin-top:30px}
.svc h3{margin-top:14px;font-size:14px;font-weight:600;line-height:26px;color:var(--heading)}
.svc p{margin:12px 8px 0;font-size:13px;line-height:23px}
.svc .go{position:absolute;left:98px;top:260px;width:36px;height:36px;border-radius:50%;background:var(--navy);display:flex;align-items:center;justify-content:center}
.svc .go svg path{stroke:#fff}
.svc.active{background:var(--navy);border-color:var(--navy)}
.svc.active h3,.svc.active p{color:#fff}
.svc.active .go{background:#fff}
.svc.active .go svg path{stroke:var(--navy)}

/* about */
.about{left:0;top:1534px;width:1200px;height:471px;background:var(--light)}
.about .photo{left:0;top:0;width:603px;height:471px;background:linear-gradient(110deg,#2e3a4a 0%,#8a7c70 35%,#d9cfc4 60%,#eceef0 100%)}
.about h2{left:618px;top:66px;font-size:27px;font-weight:700;color:var(--heading)}
.about h2 span{color:var(--navy)}
.about .frame{left:1015px;top:81px;width:73px;height:300px;border:3px solid var(--navy);border-left:none}
.about .frame2{left:778px;top:378px;width:240px;height:3px;background:var(--navy)}
.about .copy{left:618px;top:124px;width:433px;font-size:13.5px;line-height:26px;text-align:justify}
.about .copy p+p{margin-top:12px}
.about .btn{left:618px;top:355px;width:146px;height:50px}

/* team */
.team{top:2176px;width:232px;height:317px}
.team .av{width:86px;height:86px;border-radius:50%;margin:22px auto 0;background:linear-gradient(#b9b2ab,#5d5650)}
.team h3{margin-top:24px;font-size:15px;font-weight:600;color:var(--heading)}
.team .role{font-size:13px;margin-top:4px}
.team p{margin:10px 8px 0;font-size:13px;line-height:23px}
.team .soc{display:flex;gap:4px;justify-content:center;margin-top:10px}
.circ{width:26px;height:26px;border-radius:50%;border:1.5px solid #2a2a2a}

/* partners */
.partners{left:0;top:2588px;width:1200px;height:297px;background:var(--navy)}
.partners .title{color:#fff;top:60px}
.logo-box{top:144px;width:176px;height:87px;background:#fff;border-radius:3px;display:flex;align-items:center;justify-content:center}
.logo-box .badge{width:110px;height:34px;border-radius:4px;background:var(--placeholder)}
.arrow{top:170px}

/* testimonials */
.testi{top:3056px;width:315px;height:197px;text-align:left}
.testi .av{left:14px;top:14px;width:62px;height:62px;border-radius:50%;background:linear-gradient(#d8c3b0,#7d5f4a)}
.testi .who{left:88px;top:28px;font-size:13px;font-weight:600;color:var(--heading)}
.testi .who small{font-size:11px;font-weight:400;color:var(--text)}
.testi .stars{left:88px;top:48px;display:flex;gap:3px}
.testi .q{right:16px;top:30px}
.testi p{left:14px;top:106px;width:290px;font-size:14px;line-height:25px}
.tdots{left:562px;top:3283px;display:flex;gap:5px}
.tdots .ring{border-color:#222;width:14px;height:14px}
.tdots .ring.on{background:#222}

/* footer */
.footer-bg{left:0;top:3365px}
.footer h4{font-size:15px;font-weight:600;color:#fff}
.footer ul{list-style:none;margin-top:14px;font-size:13.5px;color:#fff}
.footer li{display:flex;align-items:flex-start;gap:22px;line-height:26px}
.footer li i{flex:none;width:10px;height:10px;border-radius:50%;background:var(--navy);margin-top:8px}
.footer .brand .name{color:#fff;font-size:25px}
.footer .brand .mark{width:58px;height:58px}
.footer .soc{display:flex;gap:8px}
.footer .soc .circ{border-color:#fff;width:28px;height:28px}
.footer .soc .circ.fill{background:var(--navy);border-color:var(--navy)}
.footer .rule{left:110px;top:3732px;width:978px;height:1px;background:#3b3b3e}
.footer .copy{left:0;top:3752px;width:1200px;text-align:center;color:#fff;font-size:12px}
.footer .copy b{font-weight:600}
.footer .copy span{color:var(--navy)}
</style>
</head>
<body>

<div class="abs topbar">
  <div class="abs info"><span>info@harlowsolutions.in</span><span>|</span><span>465, Lorum psum Dolore, United States</span></div>
  <div class="abs social"><span class="dot-s"></span><span class="dot-s"></span><span class="dot-s"></span></div>
  <div class="abs phone">
    <svg width="12" height="12" viewBox="0 0 24 24"><path fill="#fff" d="M6.6 10.8a15 15 0 0 0 6.6 6.6l2.2-2.2c.3-.3.7-.4 1-.2 1.1.4 2.3.6 3.6.6.6 0 1 .4 1 1V20c0 .6-.4 1-1 1A17 17 0 0 1 3 4c0-.6.4-1 1-1h3.5c.6 0 1 .4 1 1 0 1.3.2 2.5.6 3.6.1.3 0 .7-.2 1z"/></svg>
    <span>+1 (888) 888 8888</span>
  </div>
</div>

<header class="abs header">
  <div class="abs brand"><span class="mark"></span><span class="name">Harlow Solutions</span></div>
  <nav class="abs nav">
    <a class="active">HOME</a><a>ABOUT</a><a>SERVICES ⌄</a><a>INDUSTRIES</a><a>BLOG</a><a>CONTACT</a>
  </nav>
</header>

<section class="abs hero">
  <div class="abs photo" role="img" aria-label="Business professionals shaking hands in a bright office"></div>
  <svg class="abs wave" width="1200" height="664" viewBox="0 0 1200 664">
    <path d="M0 473 C 200 640 520 680 800 620 C 980 580 1100 530 1200 490 L1200 664 L0 664Z" fill="var(--navy)"/>
    <path d="M0 500 C 200 660 520 690 800 640 C 980 605 1100 560 1200 520 L1200 664 L0 664Z" fill="#fff"/>
  </svg>
  <h1 class="abs"><span>HARLOW</span> SOLUTIONS</h1>
  <p class="abs">Lorem ipsum dolor sit amet, consectetur adi<br>pis cing elit sed do eiusmod temea.</p>
  <a class="abs btn btn-solid">GET STARTED</a>
  <div class="abs dots"><span class="ring on"></span><span class="ring"></span><span class="ring"></span><span class="ring"></span></div>
</section>

<h2 class="abs title" style="top:872px"><span>OUR</span> SERVICES</h2>
<p class="abs svc-lead">Sed ut perspiciatis unde omnis iste natus error sit voluptatem accusantium doloremque laudantium, totam rem aperiam, eaque ipsa quae ab illo architecto beatae vitae dicta sunt explicabo.</p>
<div class="abs svc-btns"><a class="btn btn-solid">STAFF AUGMENTATION</a><a class="btn btn-line">OPERATION SUPPORT</a></div>

<div class="abs card svc" style="left:110px">
  <svg class="ico" width="56" height="56" viewBox="0 0 56 56" fill="none" stroke="var(--navy)" stroke-width="2"><circle cx="28" cy="22" r="10"/><circle cx="28" cy="22" r="16" stroke-dasharray="5 4"/><path d="M23 38h10M24 43h8"/></svg>
  <h3>HANDING OF<br>WORK PROJECTS</h3>
  <p>At vero eos et accusamus et ius to odio dignissimos ducimus qu iblanditiis praesenea.</p>
  <span class="go"><svg width="12" height="12" viewBox="0 0 12 12"><path d="M4 2l4 4-4 4" fill="none" stroke-width="2"/></svg></span>
</div>
<div class="abs card svc" style="left:359px">
  <svg class="ico" width="56" height="56" viewBox="0 0 56 56" fill="none" stroke="var(--navy)" stroke-width="2"><rect x="6" y="10" width="36" height="26"/><path d="M12 30l8-8 6 5 10-11M14 36l-5 14M34 36l5 14M24 36v14"/><circle cx="46" cy="10" r="5"/></svg>
  <h3>PERFORMANCE<br>MANAGEMENT</h3>
  <p>At vero eos et accusamus et ius to odio dignissimos ducimus qu iblanditiis praesenea.</p>
  <span class="go"><svg width="12" height="12" viewBox="0 0 12 12"><path d="M4 2l4 4-4 4" fill="none" stroke-width="2"/></svg></span>
</div>
<div class="abs card svc active" style="left:607px">
  <svg class="ico" width="56" height="56" viewBox="0 0 56 56" fill="none" stroke="#fff" stroke-width="2"><rect x="8" y="6" width="30" height="40"/><path d="M14 16h6v6h-6zM14 28h6v6h-6zM24 18h8M24 30h8"/><circle cx="40" cy="32" r="6"/><path d="M30 50c0-6 4-10 10-10s10 4 10 10"/></svg>
  <h3>FEEDBACK<br>MECHANISM</h3>
  <p>At vero eos et accusamus et ius to odio dignissimos ducimus qu iblanditiis praesenea.</p>
  <span class="go"><svg width="12" height="12" viewBox="0 0 12 12"><path d="M4 2l4 4-4 4" fill="none" stroke-width="2"/></svg></span>
</div>
<div class="abs card svc" style="left:856px">
  <svg class="ico" width="56" height="56" viewBox="0 0 56 56" fill="none" stroke="var(--navy)" stroke-width="2"><circle cx="20" cy="14" r="6"/><path d="M10 48V30c0-5 4-8 10-8s10 3 10 8v18"/><rect x="32" y="8" width="16" height="30"/><path d="M36 16l2 2 4-4M36 28l2 2 4-4"/></svg>
  <h3>BEHAVIORAL<br>DEVELOPMENT</h3>
  <p>At vero eos et accusamus et ius to odio dignissimos ducimus qu iblanditiis praesenea.</p>
  <span class="go"><svg width="12" height="12" viewBox="0 0 12 12"><path d="M4 2l4 4-4 4" fill="none" stroke-width="2"/></svg></span>
</div>

<section class="abs about">
  <div class="abs photo" role="img" aria-label="Team of colleagues smiling during a meeting"></div>
  <h2 class="abs"><span>ABOUT</span> HARLOW SOLUTIONS</h2>
  <div class="abs frame"></div>
  <div class="abs frame2"></div>
  <div class="abs copy">
    <p>Sed ut perspiciatis unde omnis iste natus error sit voluptatem accusantium doloremque laudantium, totam rem aperiam, eaque ipsa quae ab illo invent ore veritatis et quasi architecto beatae vitae dicta sunt explicabo. Nemo enim ipsamea.</p>
    <p>At vero eos et accusamus et iusto odio dignissimos ducimus qui blanditiis praesentium voluptatum deleniti atque corrupti quos dolores et quas sint occaecati cupiditatea.</p>
  </div>
  <a class="abs btn btn-solid">LEARN MORE</a>
</section>

<h2 class="abs title" style="top:2089px"><span>MEAT</span> OUR TEAM</h2>
<div class="abs card team" style="left:110px"><div class="av" role="img" aria-label="Portrait of team member"></div><h3>JOHN SMITH</h3><div class="role">Partner</div><p>At vero eos et accusamus et ius to odio dignissimos ducimus qu ibland ntidol umea.</p><div class="soc"><span class="circ"></span><span class="circ"></span><span class="circ"></span></div></div>
<div class="abs card team" style="left:359px"><div class="av" role="img" aria-label="Portrait of team member"></div><h3>JOHN SMITH</h3><div class="role">Partner</div><p>At vero eos et accusamus et ius to odio dignissimos ducimus qu ibland ntidol umea.</p><div class="soc"><span class="circ"></span><span class="circ"></span><span class="circ"></span></div></div>
<div class="abs card team" style="left:607px"><div class="av" role="img" aria-label="Portrait of team member"></div><h3>JOHN SMITH</h3><div class="role">Partner</div><p>At vero eos et accusamus et ius to odio dignissimos ducimus qu ibland ntidol umea.</p><div class="soc"><span class="circ"></span><span class="circ"></span><span class="circ"></span></div></div>
<div class="abs card team" style="left:856px"><div class="av" role="img" aria-label="Portrait of team member"></div><h3>JOHN SMITH</h3><div class="role">Partner</div><p>At vero eos et accusamus et ius to odio dignissimos ducimus qu ibland ntidol umea.</p><div class="soc"><span class="circ"></span><span class="circ"></span><span class="circ"></span></div></div>

<section class="abs partners">
  <h2 class="abs title">OUR PARTNERS</h2>
  <svg class="abs arrow" style="left:44px" width="32" height="32" viewBox="0 0 32 32"><circle cx="16" cy="16" r="14" fill="#2b5a86"/><path d="M19 8l-8 8 8 8" stroke="#fff" stroke-width="3" fill="none"/></svg>
  <svg class="abs arrow" style="left:1124px" width="32" height="32" viewBox="0 0 32 32"><circle cx="16" cy="16" r="14" fill="#2b5a86"/><path d="M13 8l8 8-8 8" stroke="#fff" stroke-width="3" fill="none"/></svg>
  <div class="abs logo-box" style="left:110px" role="img" aria-label="Partner badge"><span class="badge"></span></div>
  <div class="abs logo-box" style="left:312px" role="img" aria-label="Partner badge"><span class="badge"></span></div>
  <div class="abs logo-box" style="left:512px" role="img" aria-label="Partner badge"><span class="badge"></span></div>
  <div class="abs logo-box" style="left:712px" role="img" aria-label="Partner badge"><span class="badge"></span></div>
  <div class="abs logo-box" style="left:912px" role="img" aria-label="Partner badge"><span class="badge"></span></div>
</section>

<h2 class="abs title" style="top:2968px">TESTIMONIALS</h2>
<div class="abs card testi" style="left:110px">
  <div class="abs av" role="img" aria-label="Client portrait"></div>
  <div class="abs who">OLIVIA, <small>United States</small></div>
  <div class="abs stars"><svg width="70" height="10"><g fill="var(--star)"><circle cx="5" cy="5" r="4"/><circle cx="19" cy="5" r="4"/><circle cx="33" cy="5" r="4"/><circle cx="47" cy="5" r="4"/><circle cx="61" cy="5" r="4"/></g></svg></div>
  <svg class="abs q" width="44" height="36" viewBox="0 0 44 36"><path d="M0 0h18v18l-8 18H2l6-16H0zM24 0h18v18l-8 18h-8l6-16h-8z" fill="#d7dbe0"/></svg>
  <p class="abs">At vero eos et accusamus et iusto od io dignissimos ducimus qui blanditiis prae sentium voluptatum.</p>
</div>
<div class="abs card testi" style="left:443px">
  <div class="abs av" role="img" aria-label="Client portrait" style="background:linear-gradient(#c9c2ba,#3a342f)"></div>
  <div class="abs who">OLIVIA, <small>United States</small></div>
  <div class="abs stars"><svg width="70" height="10"><g fill="var(--star)"><circle cx="5" cy="5" r="4"/><circle cx="19" cy="5" r="4"/><circle cx="33" cy="5" r="4"/><circle cx="47" cy="5" r="4"/><circle cx="61" cy="5" r="4"/></g></svg></div>
  <svg class="abs q" width="44" height="36" viewBox="0 0 44 36"><path d="M0 0h18v18l-8 18H2l6-16H0zM24 0h18v18l-8 18h-8l6-16h-8z" fill="#d7dbe0"/></svg>
  <p class="abs">At vero eos et accusamus et iusto od io dignissimos ducimus qui blanditiis prae sentium voluptatum.</p>
</div>
<div class="abs card testi" style="left:775px">
  <div class="abs av" role="img" aria-label="Client portrait" style="background:linear-gradient(#e6d6c2,#a37b56)"></div>
  <div class="abs who">OLIVIA, <small>United States</small></div>
  <div class="abs stars"><svg width="70" height="10"><g fill="var(--star)"><circle cx="5" cy="5" r="4"/><circle cx="19" cy="5" r="4"/><circle cx="33" cy="5" r="4"/><circle cx="47" cy="5" r="4"/><circle cx="61" cy="5" r="4"/></g></svg></div>
  <svg class="abs q" width="44" height="36" viewBox="0 0 44 36"><path d="M0 0h18v18l-8 18H2l6-16H0zM24 0h18v18l-8 18h-8l6-16h-8z" fill="#d7dbe0"/></svg>
  <p class="abs">At vero eos et accusamus et iusto od io dignissimos ducimus qui blanditiis prae sentium voluptatum.</p>
</div>
<div class="abs tdots"><span class="ring"></span><span class="ring"></span><span class="ring on"></span><span class="ring"></span></div>

<footer class="footer">
  <svg class="abs footer-bg" width="1200" height="423" viewBox="0 0 1200 423">
    <path d="M0 170 C 250 60 500 0 760 10 C 960 20 1110 90 1200 150 L1200 423 L0 423Z" fill="var(--navy)"/>
    <path d="M0 172 C 250 70 500 14 760 24 C 950 34 1100 110 1200 185 L1200 423 L0 423Z" fill="var(--ink)"/>
  </svg>
  <div class="abs brand" style="left:110px;top:3563px"><span class="mark"></span><span class="name">Harlow Solutions</span></div>
  <div class="abs soc" style="left:174px;top:3631px"><span class="circ fill"></span><span class="circ"></span><span class="circ"></span></div>
  <div class="abs" style="left:410px;top:3495px"><h4>QUICK LINKS</h4><ul><li><i></i>Home</li><li><i></i>About</li><li><i></i>Services</li><li><i></i>Industries</li><li><i></i>Blog</li><li><i></i>Contact</li></ul></div>
  <div class="abs" style="left:612px;top:3495px"><h4>OUR SERVICES</h4><ul><li><i></i>Staff Augmentation</li><li><i></i>Operation Support</li></ul></div>
  <div class="abs" style="left:869px;top:3495px"><h4>CONTACT</h4><ul><li><i></i>465, Lorum psum Dolore,<br>United States</li><li style="margin-top:6px"><i></i>+1 (888) 888 8888</li><li style="margin-top:6px"><i></i>info@harlowsolutions.in</li></ul></div>
  <div class="abs rule"></div>
  <div class="abs copy">© 2022 <b><span>HARLOW</span> SOLUTIONS</b>. All Rights Reserved</div>
</footer>

</body>
</html>
```